Marlow's Wiring (www.marlowswiring.example)

I own and operate a telecommunication business in Dallas, Texas. We specialize in Ethernet cabling , networking, wireless implementation, security camera (CCTV) installation, Home theater systems, Audio/Video installations, Lighting

i would like a full vehicle wrap for the Vantor Roadmaster R310 Cargo Van
i will attach our company logo PDF so it can be added as well.
I am looking for a modern, sleek logo with Bold letters. i want it to scream luxury service.
please emphasize " 5 star rated on Findly and Rateo" somehow, include "CTB A+ Rated" and Or the CTB A+ logo which i will include a photo of it.
I will also attach ideas of the van designs i like from the internet. i am open to changing my business colors so feel free to suggest new logo design/colors.
No Cartoon characters or people in van design.
i would like for the van wrap to include a few key words similar to the "clear line" Van design on each side of the van wrap. Keywords can be: Network wiring | Audio | Video | Surveillance | Wi-Fi

please include my phone number 555 013 2468
and my website Marlowswiring.example

Vehicle wrap company image Requirements:
Create or convert all layered files to RGB Color Mode in Adobe Photoshop CS3 or Adobe Illustrator CS3. Do not use CMYK Color Mode.

Assign Adobe RGB (1998) Color Profile to both bitmap and vector-formatted files.

Send vector files as true vector files.

A bitmap image such as a .JPG or .TIF file, saved as an .EPS/.AI file in a vector program, such as Adobe Illustrator, does not constitute as being true vector.

Design all layered files at actual print size at 72 dpi, with at least 6” of extra bleed beyond vehicle outline.

Supplied art files must be in high resolution. If you are unsure of the resolution of an image, play it safe and always go big! The higher the resolution in dots per inch (dpi) and the bigger the dimensions, the less chance of the image(s) will have of pixelation.

Do not resize art files down for uploading purposes. Instead, compress all files, individually

```html
<!DOCTYPE html>
<html lang="en">
<head>
<meta charset="utf-8">
<title>Marlow's Wiring – Van Wrap</title>
<link rel="stylesheet" href="https://fonts.googleapis.com/css2?family=Barlow:wght@400;500&family=Montserrat:wght@600&family=Michroma&family=Ubuntu:wght@500;700&display=swap">
<style>
  :root{
    --bg:#ffffff;
    --panel:#e1e1e3;
    --ink:#111111;
    --charcoal:#2e2e30;
    --gold:#c3a06a;
    --badge:#2d6ca5;
  }
  *{margin:0;padding:0;box-sizing:border-box}
  html,body{width:805px;height:1200px;overflow:hidden;background:var(--bg)}
  .stage{position:relative;width:805px;height:1200px}
  .wrap-panel{position:absolute;left:0;top:0}
  .abs{position:absolute;white-space:nowrap}
  .center{transform:translateX(-50%);text-align:center}

  .service-list{font-family:"Barlow",sans-serif;font-weight:500;font-size:11.5px;line-height:15px;color:var(--gold);list-style:none}
  .service-list .indent{padding-left:9px}
  .service-list--back{color:var(--ink);font-size:12.5px;line-height:17.7px}

  .wordmark{font-family:"Montserrat",sans-serif;font-weight:600;color:var(--charcoal);text-align:center;line-height:1}
  .wordmark .name{display:block;font-size:31px;letter-spacing:.5px}
  .wordmark .trade{display:block;font-size:16px;letter-spacing:6px;margin-top:6px}
  .wordmark--back .name{font-size:24px}
  .wordmark--back .trade{font-size:13px;letter-spacing:5px;margin-top:4px}

  .mark-square{position:absolute;background:var(--gold)}

  .side-tag{font-family:"Montserrat",sans-serif;font-weight:600;color:var(--ink);font-size:12px;line-height:14px;text-align:left}
  .side-tag .dot{display:block;width:16px;height:16px;background:var(--ink);margin-bottom:6px}

  .keywords{font-family:"Barlow",sans-serif;font-size:14px;color:var(--gold);line-height:18px}
  .keywords--back{color:var(--ink);font-size:14px;line-height:19px;white-space:normal;width:170px}

  .phone{font-family:"Michroma",sans-serif;font-weight:700;font-size:22px;color:var(--ink);letter-spacing:1px;line-height:26px;-webkit-text-stroke:.8px var(--ink)}
  .phone--back{font-size:15px;line-height:18px;-webkit-text-stroke:.6px var(--ink)}

  .website{font-family:"Ubuntu",sans-serif;font-weight:700;font-size:20px;color:var(--charcoal);line-height:22px}
  .website--back{font-size:14.5px;line-height:17px}

  .rating{font-family:"Barlow",sans-serif;font-size:9.5px;line-height:10.5px;color:var(--ink);white-space:normal;width:60px}
</style>
</head>
<body>
<div class="stage">

  <!-- Driver side -->
  <svg class="wrap-panel" width="805" height="300" viewBox="0 0 805 300" aria-hidden="true">
    <rect x="14" y="38" width="778" height="230" rx="18" fill="var(--panel)"/>
    <polygon points="319,40 395,40 319,70" fill="var(--gold)"/>
    <path d="M539 181 C545 110 560 45 612 38 L735 38 C760 60 765 120 768 181 Z" fill="var(--ink)"/>
    <rect x="319" y="180" width="349" height="23" fill="var(--ink)"/>
    <rect x="319" y="204" width="282" height="29" fill="var(--gold)"/>
    <rect x="702" y="176" width="30" height="39" rx="3" fill="var(--badge)"/>
  </svg>
  <div class="mark-square" style="left:403px;top:52px;width:55px;height:58px"></div>
  <div class="abs wordmark center" style="left:430px;top:122px"><span class="name">MARLOW'S</span><span class="trade">WIRING</span></div>
  <ul class="abs service-list" style="left:576px;top:52px">
    <li>- ETHERNET CABLING</li><li>- NETWORKING</li><li>- WIRELESS IMPLEMENTATION</li>
    <li>- SECURITY CAMERA (CCTV)</li><li class="indent">INSTALLATION</li>
    <li>- HOME THEATER SYSTEMS</li><li>- AUDIO/VIDEO INSTALLATIONS</li><li>- LIGHTING</li>
  </ul>
  <div class="abs keywords center" style="left:465px;top:183px">Network wiring | Audio | Video | Surveillance | Wi-Fi</div>
  <div class="abs phone center" style="left:450px;top:206px">555 013 2468</div>
  <div class="abs website center" style="left:437px;top:240px">Marlowswiring.example</div>
  <div class="abs side-tag" style="left:216px;top:186px"><span class="dot"></span>MARLOW'S<br>WIRING</div>
  <div class="abs rating center" style="left:718px;top:223px">5 star rated on Findly and Rateo</div>

  <!-- Passenger side -->
  <svg class="wrap-panel" width="805" height="620" viewBox="0 0 805 620" aria-hidden="true">
    <rect x="14" y="368" width="778" height="230" rx="18" fill="var(--panel)"/>
    <polygon points="421,368 485,368 485,398" fill="var(--gold)"/>
    <path d="M267 508 C260 440 245 372 200 366 L70 372 C48 392 40 450 38 508 Z" fill="var(--ink)"/>
    <rect x="38" y="508" width="447" height="23" fill="var(--ink)"/>
    <rect x="215" y="532" width="270" height="29" fill="var(--gold)"/>
    <rect x="71" y="504" width="30" height="39" rx="3" fill="var(--badge)"/>
  </svg>
  <div class="mark-square" style="left:348px;top:380px;width:55px;height:58px"></div>
  <div class="abs wordmark center" style="left:375px;top:450px"><span class="name">MARLOW'S</span><span class="trade">WIRING</span></div>
  <ul class="abs service-list" style="left:73px;top:379px">
    <li>- ETHERNET CABLING</li><li>- NETWORKING</li><li>- WIRELESS IMPLEMENTATION</li>
    <li>- SECURITY CAMERA (CCTV)</li><li class="indent">INSTALLATION</li>
    <li>- HOME THEATER SYSTEMS</li><li>- AUDIO/VIDEO INSTALLATIONS</li><li>- LIGHTING</li>
  </ul>
  <div class="abs keywords center" style="left:285px;top:511px">Network wiring | Audio | Video | Surveillance | Wi-Fi</div>
  <div class="abs phone center" style="left:355px;top:534px">555 013 2468</div>
  <div class="abs website center" style="left:364px;top:568px">Marlowswiring.example</div>
  <div class="abs side-tag" style="left:527px;top:514px"><span class="dot"></span>MARLOW'S<br>WIRING</div>
  <div class="abs rating center" style="left:84px;top:551px">5 star rated on Findly and Rateo</div>

  <!-- Rear doors -->
  <svg class="wrap-panel" width="805" height="1100" viewBox="0 0 805 1100" aria-hidden="true">
    <rect x="185" y="708" width="190" height="332" rx="6" fill="var(--panel)"/>
    <rect x="377" y="708" width="190" height="332" rx="6" fill="var(--panel)"/>
  </svg>
  <div class="mark-square" style="left:257px;top:762px;width:48px;height:50px"></div>
  <div class="abs wordmark wordmark--back center" style="left:281px;top:825px"><span class="name">MARLOW'S</span><span class="trade">WIRING</span></div>
  <div class="abs keywords keywords--back center" style="left:281px;top:926px">Network wiring | Audio | Video | Surveillance | Wi-Fi</div>
  <div class="abs phone phone--back center" style="left:279px;top:1009px">555 013 2468</div>
  <ul class="abs service-list service-list--back" style="left:386px;top:740px">
    <li>- ETHERNET CABLING</li><li>- NETWORKING</li><li>- WIRELESS IMPLEMENTATION</li>
    <li>- SECURITY CAMERA (CCTV)</li><li class="indent">INSTALLATION</li>
    <li>- HOME THEATER SYSTEMS</li><li>- AUDIO/VIDEO INSTALLATIONS</li><li>- LIGHTING</li>
  </ul>
  <div class="abs website website--back center" style="left:471px;top:1009px">Marlowswiring.example</div>

</div>
</body>
</html>
```